Business Card for Ferncliff Massage

I need a business card for my massage therapy & cannabis oil practice. I already have a logo,the "massage" got edited out of this file. I will send the original soon. I need these elements to be on the card:
web: FerncliffMassage.example
ph: 417/283-9061
email: Mirela.Dawkant@mailbox.example
Other slogans, statements to consider:
Science Geek, Massage Therapist, Neuromuscular Therapy, Cannabis Spa Treatments, Raindrop Therapy, Essential Oils
Target Market(s)
women between 20 & 65, people with enough $ to afford regular massage, people who recently had a motor vehicle accident, Halvora HMP insured
Industry/Entity Type
Massage Therapy
Contact Information for Business Card
I would like to see my bear logo featured; contact details, greens & blues preferred colors.

```html
<!DOCTYPE html>
<html lang="en">
<head>
<meta charset="utf-8">
<title>Ferncliff Massage – Business Card</title>
<link href="https://fonts.googleapis.com/css2?family=Roboto:wght@400;700&display=swap" rel="stylesheet">
<style>
  :root {
    --stage: #4b4b4b;
    --card-white: #ffffff;
    --earth: #736558;
    --fern: #357f40;
    --stone: #a08a7c;
    --ink-light: #ffffff;
  }
  html, body {
    margin: 0;
    width: 1200px;
    height: 1200px;
    overflow: hidden;
    background: var(--stage);
    font-family: "Roboto", sans-serif;
  }
  .card {
    position: absolute;
    left: 279px;
    width: 643px;
    height: 365px;
    border-radius: 18px;
    overflow: hidden;
  }
  .card-front { top: 202px; background: var(--earth); }
  .card-back { top: 634px; background: var(--fern); }

  .front-shape { position: absolute; inset: 0; }

  .brand {
    position: absolute;
    display: flex;
    flex-direction: column;
    align-items: center;
  }
  .brand-dot {
    width: 100px;
    height: 100px;
    border-radius: 50%;
  }
  .brand-name {
    font-weight: 400;
    font-size: 52px;
    line-height: 1;
    margin-top: 40px;
    letter-spacing: 0.5px;
  }
  .card-front .brand { left: 40px; width: 240px; top: 72px; }
  .card-front .brand-dot { background: var(--stone); }
  .card-front .brand-name { color: var(--fern); }

  .card-back .brand { left: 0; right: 0; top: 62px; }
  .card-back .brand-dot { background: var(--ink-light); width: 120px; height: 120px; }
  .card-back .brand-name { color: var(--ink-light); font-size: 56px; }

  .holder {
    position: absolute;
    right: 36px;
    top: 194px;
    text-align: right;
    color: var(--ink-light);
  }
  .holder-name { font-weight: 700; font-size: 24px; line-height: 1.1; }
  .holder-role { font-size: 16.5px; margin-top: 2px; }

  .contacts {
    position: absolute;
    right: 36px;
    top: 274px;
    margin: 0;
    padding: 0;
    list-style: none;
    color: var(--ink-light);
    font-size: 16px;
  }
  .contacts li {
    display: flex;
    justify-content: flex-end;
    align-items: center;
    gap: 10px;
    height: 22px;
  }
  .contacts svg { width: 18px; height: 18px; flex: none; }
</style>
</head>
<body>

<section class="card card-front">
  <svg class="front-shape" viewBox="0 0 643 365" preserveAspectRatio="none" aria-hidden="true">
    <path d="M0 0 H218 C300 90 345 190 318 262 C300 312 262 345 232 365 H0 Z" fill="var(--fern)"/>
    <path d="M0 0 H203 C285 90 330 190 303 262 C285 312 248 345 218 365 H0 Z" fill="var(--card-white)"/>
  </svg>

  <div class="brand">
    <div class="brand-dot"></div>
    <div class="brand-name">Ferncliff</div>
  </div>

  <div class="holder">
    <div class="holder-name">Mirela Dawkant</div>
    <div class="holder-role">Massage Therapist</div>
  </div>

  <ul class="contacts">
    <li>417/283-9061
      <svg viewBox="0 0 20 20" aria-label="phone"><path d="M2 8 C4 3 16 3 18 8 L15 9 L14 7 C12 6 8 6 6 7 L5 9 Z" fill="#fff"/><path d="M5 10 H15 L17 17 H3 Z" fill="#fff"/><circle cx="10" cy="13" r="2" fill="var(--earth)"/></svg>
    </li>
    <li>Mirela.Dawkant@mailbox.example
      <svg viewBox="0 0 20 20" aria-label="email"><rect x="1.5" y="4" width="17" height="12" fill="#fff"/><path d="M1.5 4 L10 11 L18.5 4 M1.5 16 L8 9.5 M18.5 16 L12 9.5" stroke="var(--earth)" stroke-width="1.4" fill="none"/></svg>
    </li>
    <li>FerncliffMassage.example
      <svg viewBox="0 0 20 20" aria-label="website"><g fill="none" stroke="#fff" stroke-width="1.4"><circle cx="10" cy="10" r="8"/><ellipse cx="10" cy="10" rx="3.5" ry="8"/><path d="M2 10 H18 M3.5 6 H16.5 M3.5 14 H16.5"/></g></svg>
    </li>
  </ul>
</section>

<section class="card card-back">
  <div class="brand">
    <div class="brand-dot"></div>
    <div class="brand-name">Ferncliff</div>
  </div>
</section>

</body>
</html>
```